Business that Cleans the dishes and utensils used in private jets needs a flyer to describe its b...

I need a flyer to describe a HK based company called 'Vantor Rinsing'. We help the flight attendants to clean valuable dishes and utensils to save them time and costs. Color green is preferable. The design shall be easy to read and clear

Target Market(s)

Flight attendants and flight operations management

Industry/Entity Type

Aviation

Colors

Designer to choose colors to be used in the design.

Requirements
Must have
• Clean and professional.

```html
<!DOCTYPE html>
<html lang="en">
<head>
<meta charset="utf-8">
<title>Vantor Rinsing – Aviation Cleaning Flyer</title>
<link href="https://fonts.googleapis.com/css2?family=Open+Sans:wght@400;600;700;800&display=swap" rel="stylesheet">
<style>
  :root {
    --green: #8cc63f;
    --green-dark: #6fa92a;
    --ink: #1b1b1b;
    --charcoal: #2b2b2b;
    --graphite: #4a4a4a;
    --paper: #f2f2f2;
    --white: #ffffff;
  }
  * { margin: 0; padding: 0; box-sizing: border-box; }
  html, body { width: 979px; height: 1200px; overflow: hidden; background: var(--paper); }
  body { font-family: "Open Sans", Arial, sans-serif; color: var(--ink); }
  .flyer { position: relative; width: 979px; height: 1200px; overflow: hidden; }
  .flyer-art { position: absolute; inset: 0; }

  .brand-name {
    position: absolute; left: 29px; top: 208px;
    font-size: 38px; font-weight: 700; letter-spacing: 0.5px; color: var(--ink);
  }

  .headline {
    position: absolute; left: 29px; top: 598px; width: 720px;
    font-size: 33px; line-height: 1.3; font-weight: 700; color: var(--ink);
    text-transform: uppercase;
  }
  .headline-rule {
    position: absolute; left: 29px; top: 697px; width: 598px; height: 2px;
    background: var(--green);
  }
  .intro {
    position: absolute; left: 29px; top: 722px; width: 640px;
    font-size: 18px; line-height: 1.4; color: var(--ink);
  }

  .services-tag {
    position: absolute; left: 0; top: 796px; width: 372px; height: 42px;
    background: var(--green); border-radius: 0 22px 22px 0;
    box-shadow: 3px 3px 0 rgba(0,0,0,0.12);
    color: var(--white); font-weight: 700; font-size: 24px;
    line-height: 42px; padding-left: 29px; text-transform: uppercase;
  }

  .services-list {
    position: absolute; left: 29px; top: 860px; width: 600px;
    list-style: none; display: grid;
    grid-template-columns: 289px 289px; grid-auto-flow: column;
    grid-template-rows: repeat(4, 41px);
  }
  .services-list li {
    display: flex; align-items: center; gap: 12px;
    font-size: 17px; font-weight: 700; text-transform: uppercase;
  }
  .services-list svg { width: 22px; height: 22px; flex: none; }

  .contact {
    position: absolute; left: 29px; list-style: none;
    color: var(--white); font-size: 23px; font-weight: 600;
  }
  .contact li { display: flex; align-items: center; gap: 16px; height: 46px; }
  .contact svg { width: 34px; height: 34px; }

  .social { position: absolute; left: 728px; top: 1166px; display: flex; gap: 23px; list-style: none; }
  .social li { width: 28px; height: 28px; border: 2px solid var(--white); border-radius: 50%; }
</style>
</head>
<body>
<main class="flyer">
  <svg class="flyer-art" width="979" height="1200" viewBox="0 0 979 1200" aria-hidden="false">
    <defs>
      <linearGradient id="apronPhoto" x1="0" y1="0" x2="0" y2="1">
        <stop offset="0" stop-color="#b9a9b3"/>
        <stop offset="0.35" stop-color="#d6ccd0"/>
        <stop offset="0.55" stop-color="#8e8f96"/>
        <stop offset="1" stop-color="#5c5f66"/>
      </linearGradient>
      <linearGradient id="darkBand" x1="0" y1="0" x2="1" y2="0">
        <stop offset="0" stop-color="#6d6d6d"/>
        <stop offset="0.6" stop-color="#3a3a3a"/>
        <stop offset="1" stop-color="#151515"/>
      </linearGradient>
      <linearGradient id="footerBand" x1="0" y1="0" x2="1" y2="0">
        <stop offset="0" stop-color="#1c1c1c"/>
        <stop offset="0.45" stop-color="#4d4d4d"/>
        <stop offset="1" stop-color="#1a1a1a"/>
      </linearGradient>
      <linearGradient id="cabinTan" x1="0" y1="0" x2="1" y2="1">
        <stop offset="0" stop-color="#e9dcc4"/><stop offset="1" stop-color="#a88a62"/>
      </linearGradient>
      <linearGradient id="cabinGrey" x1="0" y1="0" x2="1" y2="1">
        <stop offset="0" stop-color="#dfe3ea"/><stop offset="1" stop-color="#6c6f76"/>
      </linearGradient>
      <linearGradient id="lavatory" x1="0" y1="0" x2="0" y2="1">
        <stop offset="0" stop-color="#c9c3d6"/><stop offset="1" stop-color="#8d87a0"/>
      </linearGradient>
    </defs>

    <rect class="hero-photo" x="0" y="0" width="979" height="620" fill="url(#apronPhoto)"
          role="img" aria-label="Photo of a passenger jet parked on a wet apron with ground crew"/>

    <path class="brand-swoosh" d="M0,0 H520 C470,190 280,300 0,318 Z" fill="var(--green)"/>
    <path class="brand-panel" d="M0,0 H498 C445,170 265,285 0,300 Z" fill="var(--white)"/>

    <path class="wave-green" d="M0,445 C220,610 600,600 979,470 V1200 H0 Z" fill="var(--green)"/>
    <path class="wave-white" d="M0,505 C240,625 620,600 979,492 V1200 H0 Z" fill="var(--white)"/>
    <path class="wave-dark" d="M0,518 C260,640 630,610 979,512 V1200 H0 Z" fill="url(#darkBand)"/>
    <path class="body-panel" d="M0,560 C260,650 560,640 720,585 C830,545 920,600 979,700 V1200 H0 Z" fill="var(--paper)"/>

    <path class="footer-band" d="M0,1068 H520 C600,1068 610,1152 700,1152 H979 V1200 H0 Z" fill="url(#footerBand)"/>

    <g class="service-photos">
      <circle cx="806" cy="541" r="102" fill="var(--green)"/>
      <circle cx="806" cy="541" r="93" fill="var(--white)"/>
      <circle cx="806" cy="541" r="86" fill="url(#cabinTan)" role="img" aria-label="Photo of a crew member wiping a table in a jet cabin"/>

      <circle cx="806" cy="783" r="102" fill="var(--green)"/>
      <circle cx="806" cy="783" r="93" fill="var(--white)"/>
      <circle cx="806" cy="783" r="86" fill="url(#cabinGrey)" role="img" aria-label="Photo of a private jet cabin with a laid dining table"/>

      <circle cx="806" cy="1026" r="102" fill="var(--green)"/>
      <circle cx="806" cy="1026" r="93" fill="var(--white)"/>
      <circle cx="806" cy="1026" r="86" fill="url(#lavatory)" role="img" aria-label="Photo of a clean aircraft lavatory"/>
    </g>
  </svg>

  <div class="brand-name">VANTOR RINSING</div>

  <h1 class="headline">Get your aircraft cleaned by<br>best aviation cleaning company</h1>
  <div class="headline-rule"></div>
  <p class="intro">We help the flight attendants to clean valuable dishes and utensils to save them time and costs.</p>

  <div class="services-tag">Our services include:</div>
  <ul class="services-list">
    <li><svg viewBox="0 0 22 22"><rect x="2" y="4" width="15" height="15" fill="none" stroke="#555" stroke-width="2"/><path d="M5 11 l4 4 l11 -12" fill="none" stroke="var(--green)" stroke-width="3"/></svg>General cleaning</li>
    <li><svg viewBox="0 0 22 22"><rect x="2" y="4" width="15" height="15" fill="none" stroke="#555" stroke-width="2"/><path d="M5 11 l4 4 l11 -12" fill="none" stroke="var(--green)" stroke-width="3"/></svg>Carpet cleaning</li>
    <li><svg viewBox="0 0 22 22"><rect x="2" y="4" width="15" height="15" fill="none" stroke="#555" stroke-width="2"/><path d="M5 11 l4 4 l11 -12" fill="none" stroke="var(--green)" stroke-width="3"/></svg>Trash removal</li>
    <li><svg viewBox="0 0 22 22"><rect x="2" y="4" width="15" height="15" fill="none" stroke="#555" stroke-width="2"/><path d="M5 11 l4 4 l11 -12" fill="none" stroke="var(--green)" stroke-width="3"/></svg>Sanitizing</li>
    <li><svg viewBox="0 0 22 22"><rect x="2" y="4" width="15" height="15" fill="none" stroke="#555" stroke-width="2"/><path d="M5 11 l4 4 l11 -12" fill="none" stroke="var(--green)" stroke-width="3"/></svg>Dishes and utensils</li>
    <li><svg viewBox="0 0 22 22"><rect x="2" y="4" width="15" height="15" fill="none" stroke="#555" stroke-width="2"/><path d="M5 11 l4 4 l11 -12" fill="none" stroke="var(--green)" stroke-width="3"/></svg>Bathroom detailing</li>
    <li><svg viewBox="0 0 22 22"><rect x="2" y="4" width="15" height="15" fill="none" stroke="#555" stroke-width="2"/><path d="M5 11 l4 4 l11 -12" fill="none" stroke="var(--green)" stroke-width="3"/></svg>Vacuuming</li>
    <li><svg viewBox="0 0 22 22"><rect x="2" y="4" width="15" height="15" fill="none" stroke="#555" stroke-width="2"/><path d="M5 11 l4 4 l11 -12" fill="none" stroke="var(--green)" stroke-width="3"/></svg>Kitchen cleaning</li>
  </ul>

  <ul class="contact" style="top:1097px">
    <li>
      <svg viewBox="0 0 34 34"><circle cx="17" cy="17" r="17" fill="var(--green)"/><path d="M11 9 c-2 2 -2 6 2 11 s9 7 11 5 l1 -1 -4 -4 -2 2 c-2 -1 -4 -3 -5 -5 l2 -2 -4 -4 z" fill="var(--white)"/></svg>
      012 555 0188
    </li>
    <li>
      <svg viewBox="0 0 34 34"><circle cx="17" cy="17" r="17" fill="var(--green)"/><circle cx="17" cy="17" r="9" fill="none" stroke="var(--white)" stroke-width="2"/><ellipse cx="17" cy="17" rx="4" ry="9" fill="none" stroke="var(--white)" stroke-width="1.6"/><path d="M8 17 H26" stroke="var(--white)" stroke-width="1.6"/></svg>
      www.VantorRinsing.com
    </li>
  </ul>

  <ul class="social" aria-label="Social channels">
    <li></li><li></li><li></li><li></li>
  </ul>
</main>
</body>
</html>
```